Letterhead for denture company

We need a letterhead designed for our denture company called "Brightmolars" We have attached the logo and business card with the colours on them that we like

Target Market(s)

Everyone aged 45+

Industry/Entity Type

Dental Clinic

Font styles to use
Serif
Sans Serif

Colors
3276b5
f37122

Requirements
Must have
• The colours used in our business card
• Be bold and modern
• Thick fonts
• Logo
Nice to have
• Elements that could tie in nicely with any future signage or website upgrades
Should not have
• Thin font
• Should not be too busy

```html
<!DOCTYPE html>
<html lang="en">
<head>
<meta charset="utf-8">
<title>Brightmolars Letterhead</title>
<link rel="stylesheet" href="https://fonts.googleapis.com/css2?family=Open+Sans:wght@400;600;700;800&display=swap">
<style>
  :root {
    --brand-blue: #3276b5;
    --brand-blue-deep: #1f66ad;
    --brand-orange: #f37122;
    --paper: #ffffff;
    --ink: #2b2b2b;
    --muted: #8c8f96;
    --watermark: #eef0f7;
    --backdrop: #8a8279;
  }
  * { box-sizing: border-box; margin: 0; padding: 0; }
  html, body {
    width: 1200px;
    height: 795px;
    overflow: hidden;
  }
  body {
    background: var(--backdrop);
    font-family: "Open Sans", Arial, sans-serif;
    position: relative;
  }
  .letterhead {
    position: absolute;
    left: 331px;
    top: 18px;
    width: 538px;
    height: 760px;
    background: var(--paper);
    overflow: hidden;
    box-shadow: 0 2px 8px rgba(0,0,0,0.18);
  }
  .watermark {
    position: absolute;
    left: 130px;
    top: 205px;
    width: 290px;
    height: 290px;
    border-radius: 50%;
    background: var(--watermark);
  }
  .sender-address {
    position: absolute;
    left: 372px;
    top: 40px;
    font-style: normal;
    font-size: 7px;
    line-height: 9.5px;
    color: var(--ink);
    font-weight: 600;
  }
  .sender-address .sender-name {
    color: var(--brand-blue);
    font-weight: 700;
  }
  .sender-address .sender-web {
    color: var(--brand-blue);
    font-weight: 400;
  }
  .brand {
    position: absolute;
    left: 40px;
    top: 140px;
    display: flex;
    align-items: center;
    gap: 9px;
  }
  .brand-square {
    width: 30px;
    height: 30px;
    background: var(--brand-blue-deep);
  }
  .brand-name {
    font-size: 19px;
    font-weight: 800;
    color: var(--brand-blue-deep);
    letter-spacing: 0.5px;
    line-height: 1;
  }
  .brand-tagline {
    font-size: 7.5px;
    font-weight: 600;
    color: var(--muted);
    letter-spacing: 1.6px;
    margin-top: 4px;
  }
  .footer-wave {
    position: absolute;
    left: 0;
    top: 0;
    width: 538px;
    height: 760px;
  }
  .contact-list {
    position: absolute;
    left: 30px;
    top: 688px;
    list-style: none;
    color: var(--paper);
    font-size: 9px;
    line-height: 13px;
    font-weight: 600;
  }
  .contact-list li {
    display: flex;
    align-items: center;
    gap: 6px;
  }
  .contact-icon {
    width: 9px;
    height: 9px;
    border-radius: 50%;
    background: var(--brand-orange);
    display: inline-flex;
    align-items: center;
    justify-content: center;
  }
  .contact-icon svg { width: 6px; height: 6px; }
</style>
</head>
<body>
  <main class="letterhead">
    <div class="watermark" role="img" aria-label="Faint brand mark watermark"></div>

    <address class="sender-address">
      <div class="sender-name">Brightmolars</div>
      <div>14 Kowhai Street</div>
      <div>Harbour View, Auckland 0612</div>
      <div class="sender-web">www.brightmolars.co.nz</div>
    </address>

    <div class="brand">
      <div class="brand-square"></div>
      <div>
        <div class="brand-name">BRIGHTMOLARS</div>
        <div class="brand-tagline">CARE FOR EVERY SMILE</div>
      </div>
    </div>

    <svg class="footer-wave" viewBox="0 0 538 760" aria-hidden="true">
      <path d="M0,668 C110,668 170,722 290,714 C400,706 480,680 538,604 L538,760 L0,760 Z" fill="var(--brand-blue-deep)"/>
      <path d="M0,657 C110,657 170,711 290,703 C400,695 476,668 538,592" fill="none" stroke="var(--brand-orange)" stroke-width="5"/>
      <path d="M300,693 C405,684 474,656 538,580" fill="none" stroke="var(--brand-blue-deep)" stroke-width="3"/>
    </svg>

    <ul class="contact-list">
      <li>
        <span class="contact-icon"><svg viewBox="0 0 10 10"><path d="M2,1 L4,1 L4.6,3 L3.5,4 C4,5.3 4.8,6 6,6.5 L7,5.4 L9,6 L9,8 C5,8.5 1.5,5 2,1 Z" fill="#fff"/></svg></span>
        0800 47 2310
      </li>
      <li>
        <span class="contact-icon"><svg viewBox="0 0 10 10"><rect x="1" y="3" width="8" height="5" rx="1" fill="#fff"/><rect x="3" y="1" width="4" height="3" fill="#fff"/></svg></span>
        09 521 6684
      </li>
      <li>
        <span class="contact-icon"><svg viewBox="0 0 10 10"><rect x="1" y="2.5" width="8" height="5.5" fill="#fff"/><path d="M1,2.5 L5,6 L9,2.5" fill="none" stroke="#f37122" stroke-width="0.9"/></svg></span>
        mia@brightmolars.co.nz
      </li>
      <li>
        <span class="contact-icon"><svg viewBox="0 0 10 10"><circle cx="5" cy="5" r="3.6" fill="none" stroke="#fff" stroke-width="1"/><path d="M1.4,5 L8.6,5 M5,1.4 C3.4,3.5 3.4,6.5 5,8.6 M5,1.4 C6.6,3.5 6.6,6.5 5,8.6" fill="none" stroke="#fff" stroke-width="0.7"/></svg></span>
        www.brightmolars.co.nz
      </li>
    </ul>
  </main>
</body>
</html>
```